Billboard For Marcus Delvane

Need a Billboard 8ft. High x 16ft. Long. Ive attached a former billboard and looking for the same thing just updated with:
Wardens Guild Award Logo - 2020, 2022
Summit Lantern award Logo - 2022

Thanks.

```html
<!DOCTYPE html>
<html lang="en">
<head>
<meta charset="utf-8">
<title>Billboard – Marcus Delvane</title>
<link href="https://fonts.googleapis.com/css2?family=Montserrat:ital,wght@0,400;0,600;0,700;0,800;1,800;1,900&display=swap" rel="stylesheet">
<style>
  :root{
    --ink:#111111;
    --red:#e0202b;
    --stage:#e9edf1;
    --board-top:#ffffff;
    --board-bottom:#d9dadc;
    --photo-light:#cfd3d9;
    --photo-mid:#8a93a3;
    --photo-blue:#2f4f8c;
    --badge:#c23a3a;
    --grey:#555555;
  }
  *{box-sizing:border-box;margin:0;padding:0}
  html,body{width:1200px;height:960px;overflow:hidden}
  body{background:var(--stage);font-family:"Montserrat",Arial,sans-serif;color:var(--ink);position:relative}

  .billboard{position:absolute;left:0;top:180px;width:1200px;height:600px;overflow:hidden;
    background:linear-gradient(180deg,var(--board-top) 0%,#f3f3f4 55%,var(--board-bottom) 100%)}

  .agent-photo{position:absolute;left:0;top:70px;width:560px;height:530px;
    background:linear-gradient(180deg,var(--photo-light) 0%,var(--photo-mid) 45%,var(--photo-blue) 62%,var(--photo-blue) 100%);
    border-top-right-radius:260px 200px}

  .headline{position:absolute;left:392px;top:36px;font-weight:900;font-style:italic;
    font-size:78px;line-height:.98;letter-spacing:-1px;text-transform:uppercase;white-space:nowrap}
  .headline .line{display:block}
  .headline .line-2{padding-left:94px}
  .headline .accent{color:var(--red)}

  .info{position:absolute;left:560px;top:200px;width:580px;text-align:center}
  .agent-name{font-weight:800;font-size:38px;letter-spacing:.5px;text-transform:uppercase;line-height:1;white-space:nowrap}
  .agent-title{font-weight:600;font-size:13px;letter-spacing:3px;text-transform:uppercase;margin-top:4px}
  .phone-box{margin:6px auto 0;width:570px;height:96px;border:5px solid var(--red);border-radius:22px;
    display:flex;align-items:center;justify-content:center}
  .phone{color:var(--red);font-weight:700;font-size:68px;letter-spacing:1px;line-height:1;white-space:nowrap}
  .tagline{margin-top:12px;font-weight:800;font-size:22px;letter-spacing:.5px;text-transform:uppercase;white-space:nowrap}
  .tagline em{color:var(--red);font-style:italic}

  .awards{margin-top:22px;display:flex;justify-content:center;gap:40px}
  .award{display:flex;align-items:center;gap:10px;text-align:left}
  .award-seal{flex:none;width:46px;height:46px;border-radius:50%;background:var(--ink)}
  .award-text{font-weight:600;font-size:10px;line-height:1.2;text-transform:uppercase;white-space:nowrap}
  .award-text strong{display:block;font-weight:600;font-size:19px;line-height:1.05}

  .footer-row{margin-top:20px;display:flex;justify-content:center;align-items:center;gap:36px}
  .partner-badge{flex:none;width:60px;height:34px;background:var(--badge);border-radius:4px}
  .brokerage{text-align:left}
  .brokerage-main{display:flex;align-items:center;gap:8px}
  .brokerage-square{width:18px;height:18px;background:var(--red)}
  .brokerage-name{font-weight:800;font-size:18px;text-transform:uppercase;white-space:nowrap}
  .brokerage-sub{margin-left:26px;font-size:9px;font-weight:600;color:var(--grey);text-transform:uppercase;white-space:nowrap}
  .socials{display:flex;gap:16px}
  .social{font-weight:800;font-size:16px;color:var(--red);white-space:nowrap}
</style>
</head>
<body>
  <main class="billboard">
    <div class="agent-photo" role="img" aria-label="Portrait of the sales representative in a blue shirt and tie"></div>

    <h1 class="headline">
      <span class="line">Buying or</span>
      <span class="line line-2">Selling? <span class="accent">Call</span></span>
    </h1>

    <section class="info">
      <p class="agent-name">Marcus Delvane</p>
      <p class="agent-title">Sales Representative</p>
      <div class="phone-box"><span class="phone">613.555.0148</span></div>
      <p class="tagline">Focused, driven, and <em>experienced!</em></p>

      <div class="awards">
        <div class="award">
          <span class="award-seal"></span>
          <p class="award-text">Harborline<strong>Summit Lantern</strong>Award 2022</p>
        </div>
        <div class="award">
          <span class="award-seal"></span>
          <p class="award-text">Harborline<strong>Wardens Guild</strong>Award 2020, 2022</p>
        </div>
      </div>

      <div class="footer-row">
        <span class="partner-badge"></span>
        <div class="brokerage">
          <div class="brokerage-main">
            <span class="brokerage-square"></span>
            <span class="brokerage-name">Harborline Realty</span>
          </div>
          <p class="brokerage-sub">Team Realty, Brokerage</p>
        </div>
        <div class="socials">
          <span class="social">Chatterly</span>
          <span class="social">Photoloop</span>
        </div>
      </div>
    </section>
  </main>
</body>
</html>
```